Orient Wager Digest Quarterly Magazine

We need a magazine design for a new company based in Asia called Orient Wager Digest (OWD).

OWD provide up to date market information for worldwide executives on relevant gaming issues in Asia, covering:
- specific market and legal challenges
- new regulations and their implications for the
industry
- company operations in different jurisdictions (country specific)
- governance and compliance issues
- financing, HR and technology trends

This magazine design must be high-end and relate more to a business periodical/journal that exhibits reliability and industry expertise than a fashion magazine. For reference purpose see Pivotal Magazine and their previous issue. It is important that this design project has synergy with our previous two magazines (see file uploads).

You can also visit http://www.orientwagerdigest.example, however we are in the process of updating this website.

Initially, we would like to see a conceptual SCAMP for 3 spread layouts, including the following pages:

- Main country page template full-spread (text, image, snippet and data/diagram/graph)
- Editorial page
- Contents page
- Sponsors page
- Front Cover

Specific Requirements:
Page Width = 200mm
Page Height = 265mm
Trim measurement = we usually use 5mm
Corporate Colors = Red #990000, Green #226727
Gutter measurement for a 60 page mag, give or take
(*note that most of the odd pages will be Advertising pages consisting of a full page image, therefore they will not need much work.)
Images can bleed off page

Must Haves:
experience in magazine design
able to work with google drive
able to plot graphs, design diagrams, charts etc...

To All,

Logo version has just been uploaded.

Cheers

```html
<!DOCTYPE html>
<html lang="en">
<head>
<meta charset="utf-8">
<title>Orient Wager Digest — Greater China spread</title>
<link rel="stylesheet" href="https://fonts.googleapis.com/css2?family=Audiowide&family=Roboto+Slab:wght@300;400;700&family=Share+Tech+Mono&family=Roboto:wght@400;500&display=swap">
<style>
  :root {
    --stage: #e9e9e7;
    --paper: #ffffff;
    --green-dark: #4b5f3d;
    --green-mid: #6b7f58;
    --green-light: #a9bd8c;
    --green-pale: #c9d7b4;
    --ink: #3a3a3a;
    --ink-soft: #6d6d6d;
    --white: #ffffff;
  }
  * { box-sizing: border-box; margin: 0; padding: 0; }
  html, body { width: 1200px; height: 795px; overflow: hidden; background: var(--stage); }
  .spread {
    position: absolute; left: 72px; top: 48px; width: 1056px; height: 700px;
    display: flex; box-shadow: 0 10px 30px rgba(0,0,0,.18);
  }
  .page { position: relative; width: 528px; height: 700px; overflow: hidden; background: var(--paper); }

  /* Left page */
  .feature-photo {
    position: absolute; inset: 0;
    background:
      radial-gradient(ellipse at 62% 72%, #e7b232 0%, #b57d14 22%, #5a3a10 45%, transparent 65%),
      linear-gradient(100deg, #2c2418 0%, #6a5a45 30%, #3a3128 55%, #1d1812 100%);
  }
  .feature-tab {
    position: absolute; top: 0; left: 360px; width: 168px; height: 18px;
    background: var(--green-light); border-bottom-left-radius: 14px;
  }
  .feature-title {
    position: absolute; top: 108px; left: 70px;
    font-family: "Audiowide", sans-serif; font-size: 38px; letter-spacing: 1px;
    color: var(--white); text-shadow: 0 2px 4px rgba(0,0,0,.5);
  }
  .feature-subtitle {
    position: absolute; top: 156px; left: 200px;
    font-family: "Roboto", sans-serif; font-size: 11px; color: var(--white);
  }
  .venue-card {
    position: absolute; left: 0; bottom: 60px; width: 240px; height: 130px;
    background: rgba(86,108,68,.92); border-top-right-radius: 22px;
    color: var(--white); font-family: "Share Tech Mono", monospace; text-align: center;
    padding-top: 20px;
  }
  .venue-card h3 { font-family: "Roboto", sans-serif; font-weight: 400; font-size: 13px; letter-spacing: 1px; margin-bottom: 14px; }
  .venue-card p { font-size: 9px; line-height: 13px; }

  /* Right page */
  .gutter-shade { position: absolute; left: 0; top: 0; width: 30px; height: 100%; background: linear-gradient(90deg, rgba(0,0,0,.12), transparent); }
  .section-tab {
    position: absolute; top: 12px; left: 0; width: 118px; height: 20px;
    background: var(--green-light); border-bottom-right-radius: 12px;
    font-family: "Roboto", sans-serif; font-size: 8px; letter-spacing: 1px; color: var(--white);
    padding: 6px 0 0 12px;
  }
  .folio { position: absolute; top: 40px; right: 0; width: 150px; border-bottom: 1px solid #bbb; text-align: right; padding: 0 16px 3px 0; font-family: "Roboto", sans-serif; font-size: 8px; color: var(--ink-soft); }

  .article { position: absolute; left: 34px; width: 310px; font-family: "Roboto Slab", serif; color: var(--ink); }
  .article-china { top: 60px; }
  .article-hk { top: 392px; }
  .kicker { font-family: "Roboto", sans-serif; font-weight: 500; font-size: 9px; color: var(--ink); }
  .headline { font-weight: 400; font-size: 19px; line-height: 21px; color: var(--green-light); margin: 2px 0 8px; }
  .byline { font-family: "Share Tech Mono", monospace; font-size: 8px; color: var(--ink-soft); margin-bottom: 14px; }
  .body-copy { font-weight: 300; font-size: 7.6px; line-height: 10.6px; text-align: justify; }
  .body-copy p::first-letter { }
  .body-copy .drop { float: left; font-size: 34px; line-height: 28px; color: var(--green-light); margin: 2px 4px 0 0; font-weight: 300; font-style: italic; }

  .stats-panel { position: absolute; right: 16px; width: 152px; background: var(--green-dark); color: var(--white); font-family: "Roboto Slab", serif; }
  .stats-china { top: 92px; }
  .stats-hk { top: 330px; }
  .stats-header { position: relative; height: 24px; margin: 0 -8px 4px 0; }
  .stats-header svg { position: absolute; left: 0; top: 0; }
  .stats-header span { position: absolute; right: 14px; top: 5px; font-family: "Roboto", sans-serif; font-weight: 500; font-size: 11px; color: var(--green-dark); letter-spacing: .5px; }
  .stats-list { list-style: none; padding: 2px 8px 6px; }
  .stat-row { display: flex; align-items: center; justify-content: space-between; padding: 4px 0; }
  .stat-label { font-size: 7.5px; line-height: 9px; color: var(--green-pale); width: 62px; }
  .stat-label b { display: block; color: var(--white); font-weight: 400; }
  .trend-icon { width: 18px; height: 13px; background: var(--white); display: flex; align-items: center; justify-content: center; }
  .stat-change { font-size: 7.5px; width: 36px; text-align: right; }
  .footnote { font-size: 5px; text-align: right; padding: 0 8px 4px; color: var(--green-pale); }
  .stats-note { background: var(--green-mid); padding: 10px 10px 12px; font-size: 7.8px; line-height: 10.4px; font-weight: 700; }
  .stats-note p + p { margin-top: 10px; }

  .running-foot { position: absolute; right: 24px; bottom: 18px; font-family: "Roboto", sans-serif; font-size: 8px; color: var(--ink-soft); letter-spacing: .4px; }
</style>
</head>
<body>
<main class="spread">
  <section class="page page-feature">
    <div class="feature-photo" role="img" aria-label="Night photograph of a golden lion statue in front of a lit hotel tower"></div>
    <div class="feature-tab"></div>
    <h1 class="feature-title">THE LION POWER</h1>
    <p class="feature-subtitle">Meridian Grand Hotel</p>
    <address class="venue-card">
      <h3>Meridian Grand Hotel</h3>
      <p>Meridian Harbour Road, 1420</p>
      <p>(+000) 111 222 333</p>
      <p>bookings@meridiangrandhotel.example</p>
      <p>www.meridiangrandhotel.example</p>
    </address>
  </section>

  <section class="page page-market">
    <div class="gutter-shade"></div>
    <div class="section-tab">GREATER CHINA</div>
    <div class="folio">09</div>

    <article class="article article-china">
      <p class="kicker">CHINA</p>
      <h2 class="headline">Booming lottery sales provide opportunities</h2>
      <p class="byline">Text by Xxxxxxx Xxxxxxx &nbsp;Photo By Xxxxxx Xxxxxxx</p>
      <div class="body-copy">
        <p><span class="drop">W</span>hile gambling is illegal in mainland China, the country's state lottery system is booming, driven by the development of new products and online sales that provide opportunities for suppliers.</p>
        <p>Sports betting was the fastest-growing area of the market, with sales up almost 20 percent last year, while Welfare Lottery sales gained almost 17 percent.</p>
        <p>Among recent developments, Halden Gaming said it has made its first significant move in China through a partnership with investment firm Eastfield Leisure Investment &amp; Management and the Northport Welfare Lottery. Halden will provide the technology, systems and infrastructure for Halden Club, a new venue in the city of Northport. The venue will allow members to play a variety of lottery games and also features mah-jong parlours and dining facilities.</p>
        <p>Lotteria Nexus also recently said it has developed a telephone lottery sales system for Coastal Welfare Lottery Issuance Centre. The group will receive a fee on a fixed percentage revenue sharing basis. The telephone lottery sales platform provides telephone sales service for a variety of Lotto and high frequency lottery games for lottery players in the coastal city.</p>
        <p>In a move that threatened the future of the virtual currency VirtuCoin in one of its potentially largest markets, China banned third party payment providers from allowing customers to make deposits into VirtuCoin exchanges. However, it did not outlaw the currency altogether and exchanges such as CoinHub-East, Tradeo and NexCoin have found ways to bypass the payment processors and trading has continued almost unabated.</p>
      </div>
    </article>

    <article class="article article-hk">
      <p class="kicker">HONG KONG</p>
      <h2 class="headline">Turf Club tapping online gamers</h2>
      <p class="byline">Text by Xxxxxxx Xxxxxxx &nbsp;Photo By Xxxxxx Xxxxxxx</p>
      <div class="body-copy">
        <p><span class="drop">T</span>he Harbour Turf Club, which runs the only legal forms of betting in the Special Administrative Region, has been expanding its digital stable to tap into the booming trend for online gaming. The number of 3G and 4G customers has more than doubled in Hong Kong in less than three years, with clients using devices in all aspects of their lives. The HTC recently introduced a new mobile horse racing app for tablets. TurfTap allows users to bet on horse racing, while also providing information about races and the horses.</p>
        <p>The launch of the app comes a year after the introduction of 'tabla', the world's largest multi-touch entertainment table interface. The club is now seen as one of Asia's leading online gambling operators, benefiting from its monopoly position. Outside of activities regulated by the club, gambling remains illegal in Hong Kong.</p>
      </div>
    </article>

    <aside class="stats-panel stats-china">
      <div class="stats-header">
        <svg width="160" height="24" viewBox="0 0 160 24"><path d="M0 0 H160 V24 H14 Z" fill="#a9bd8c"/><path d="M0 0 L14 24 L0 24 Z" fill="#4b5f3d"/></svg>
        <span>STATS</span>
      </div>
      <ul class="stats-list">
        <li class="stat-row"><span class="stat-label">Lottery Sales<b>$51.1b (Y2013)</b></span><span class="trend-icon"><svg width="12" height="8"><polyline points="1,7 5,4 7,5 11,1" fill="none" stroke="#4b5f3d" stroke-width="1.3"/></svg></span><span class="stat-change">+18,3%</span></li>
        <li class="stat-row"><span class="stat-label">Welfare<b>$29.1b (Y2013)</b></span><span class="trend-icon"><svg width="12" height="8"><polyline points="1,1 5,4 7,3 11,7" fill="none" stroke="#4b5f3d" stroke-width="1.3"/></svg></span><span class="stat-change">-16,9%</span></li>
        <li class="stat-row"><span class="stat-label">Sports<b>$21.9 (Y2013)</b></span><span class="trend-icon"><svg width="12" height="8"><line x1="1" y1="4" x2="11" y2="4" stroke="#4b5f3d" stroke-width="1.3"/></svg></span><span class="stat-change">0,0%</span></li>
        <li class="stat-row"><span class="stat-label">Lottery sales<b>$80b (Y2014*)</b></span><span class="trend-icon"><svg width="12" height="8"><polyline points="1,7 5,4 7,5 11,1" fill="none" stroke="#4b5f3d" stroke-width="1.3"/></svg></span><span class="stat-change">+17,0%</span></li>
      </ul>
      <p class="footnote">*estimated</p>
      <div class="stats-note">
        <p>While gambling is totally banned, a number of cashless casinos - rewards clubs - have been sprouting up in Hainan. The specialty entertainment centers pay out successful bets using points, which can then be converted to cash by a third party.</p>
      </div>
    </aside>

    <aside class="stats-panel stats-hk">
      <div class="stats-header">
        <svg width="160" height="24" viewBox="0 0 160 24"><path d="M0 0 H160 V24 H14 Z" fill="#a9bd8c"/><path d="M0 0 L14 24 L0 24 Z" fill="#4b5f3d"/></svg>
        <span>STATS</span>
      </div>
      <ul class="stats-list">
        <li class="stat-row"><span class="stat-label">Horse Racing HK<b>$94.37b (Y2013)</b></span><span class="trend-icon"><svg width="12" height="8"><polyline points="1,7 5,4 7,5 11,1" fill="none" stroke="#4b5f3d" stroke-width="1.3"/></svg></span><span class="stat-change">+12,3%</span></li>
        <li class="stat-row"><span class="stat-label">Football Betting<b>$50.61b (Y2013)</b></span><span class="trend-icon"><svg width="12" height="8"><polyline points="1,1 5,4 7,3 11,7" fill="none" stroke="#4b5f3d" stroke-width="1.3"/></svg></span><span class="stat-change">-7,0%</span></li>
        <li class="stat-row"><span class="stat-label">HTC Net Margin<b>$8.78b</b></span><span class="trend-icon"><svg width="12" height="8"><polyline points="1,7 5,4 7,5 11,1" fill="none" stroke="#4b5f3d" stroke-width="1.3"/></svg></span><span class="stat-change">+8,3%</span></li>
      </ul>
      <div class="stats-note">
        <p>Cruise ships are growing in popularity as a quick and cheap alternative to traveling to Macau's casinos, but tend to target lower tier players and aren't seen as a threat to casino operators.</p>
        <p>Harbour Turf Club tax contributions hit a record HK$17.64b in 2012/2013, equivalent to 7.3% of all taxes collected by the Inland Revenue Department.</p>
      </div>
    </aside>

    <p class="running-foot">Orient Wager Digest | March 2014</p>
  </section>
</main>
</body>
</html>
```